After school program registration flyer

We need a registration flyer for our extracurricular dance clubs that are held after school or during lunch inside schools and childcare centre across Canada. For more general information, we suggest you visit our website: www.mopvelta.com.

The flyers are used to capture the interest of students (usually in Kindergarten to Grade 4) and their parents. Parents enrol their child in the club which takes place in the school or childcare centre.

We are asking you to design the front of the flyer... the first thing that students and parents see. It should capture the imagination of children, but reassure parents that this is a well-controlled, educational experience that will benefit their child.

FYI - On the back of the flyer we will add specific information for each school. You should not be concerned about the back of the flyer.

Text:
High Energy Hip Hop Dance Club At Your School
Dance is Fun! Dance is Cool! Dance is Great Exercise!
Excellent for Boys and Girls. No previous experience required.

Warm-up, Stretch, And Move to Great Music
Learn group routines.
Create your choreography.

Get a FREE dance-along DVD each term. $25 value each.

REGISTER TODAY!
Online Registration: Go to www.mopvelta.com
Registration Hotline: Call 416-729-3546 ext 517
See reverse side for details

IMPORTANT NOTE TO PARENTS
Educational studies confirm that children who participate in extracurricular programs enjoy an increase sense of accomplishment, competence and self-esteem, translating into improved academic performance.

Target Market(s)

Boys and girls in Kindergarten to Grade 4 and their parents

Industry/Entity Type

Childcare

Requirements
Must have
• Our logo

Photos of happy children dancing. We will provide you with photographs, probably more than what you need so you can select the ones that work best for your design.

```html
<!DOCTYPE html>
<html lang="en">
<head>
<meta charset="utf-8">
<title>Hip Hop Dance Club Registration Flyer</title>
<link rel="stylesheet" href="https://fonts.googleapis.com/css2?family=Arimo:ital,wght@0,400;0,700;1,700&display=swap">
<style>
  :root {
    --brand-orange: #f26a21;
    --banner-red: #e8452c;
    --sky-blue: #bfe3f5;
    --sky-blue-deep: #8fcdea;
    --lime: #8dc63f;
    --lime-deep: #5fa62f;
    --register-red: #d9261c;
    --white: #ffffff;
    --ink: #2b2b2b;
  }
  * { box-sizing: border-box; margin: 0; padding: 0; }
  html, body { width: 872px; height: 1200px; overflow: hidden; background: var(--white); }
  body { font-family: "Arimo", Arial, sans-serif; }

  .flyer { position: relative; width: 872px; height: 1200px; background: var(--white); overflow: hidden; }

  .brand { position: absolute; left: 24px; top: 22px; display: flex; align-items: center; gap: 12px; }
  .brand-dot { width: 34px; height: 34px; border-radius: 50%; background: var(--lime); }
  .brand-name { font-weight: 700; font-size: 54px; color: var(--brand-orange); letter-spacing: 1px; line-height: 1; }

  .title-band {
    position: absolute; left: 0; top: 122px; width: 872px; height: 62px;
    background: var(--banner-red); color: var(--white);
    display: flex; align-items: center; justify-content: center;
    font-weight: 700; font-size: 35px;
  }

  .intro-panel {
    position: absolute; left: 0; top: 184px; width: 872px; height: 396px;
    background: linear-gradient(180deg, var(--sky-blue) 0%, var(--sky-blue-deep) 100%);
  }
  .slogans {
    position: absolute; left: 28px; top: 200px; width: 820px;
    display: flex; justify-content: space-between;
    font-weight: 700; font-style: italic; font-size: 27px; color: var(--lime-deep);
  }

  .photo { position: absolute; }
  .photo-circle-top {
    left: 28px; top: 250px; width: 206px; height: 206px; border-radius: 50%;
    border: 6px solid var(--white);
    background: radial-gradient(circle at 50% 40%, #d9c6b4 0%, #8a6b56 55%, #3a2e2a 100%);
  }

  .features { position: absolute; left: 272px; top: 258px; color: var(--white); font-weight: 700; font-size: 24px; line-height: 1.3; text-shadow: 0 1px 2px rgba(0,0,0,.25); }
  .features p + p { margin-top: 22px; }

  .register-box {
    position: absolute; left: 612px; top: 418px; width: 244px; height: 152px;
    background: var(--white); border: 3px dashed var(--register-red);
    transform: rotate(-3deg);
    color: var(--register-red); text-align: center; padding: 10px 8px;
    font-weight: 700;
  }
  .register-title { font-size: 23px; margin-bottom: 6px; }
  .register-box p { font-size: 15px; line-height: 1.25; }
  .register-box p + p { margin-top: 5px; }

  .offer-stripe {
    position: absolute; left: 0; top: 530px; width: 596px; height: 44px;
    background: var(--brand-orange); color: var(--white);
    display: flex; align-items: center; padding-left: 18px;
    font-weight: 700; font-size: 19px;
  }

  .photo-main {
    left: 0; top: 580px; width: 660px; height: 620px;
    background: linear-gradient(160deg, #f2c27a 0%, #e48a52 35%, #6c8fb8 70%, #3f5f86 100%);
  }

  .parents-column {
    position: absolute; left: 660px; top: 580px; width: 212px; height: 620px;
    background: linear-gradient(180deg, var(--sky-blue-deep) 0%, var(--sky-blue) 100%);
    padding: 34px 14px 0 18px; color: var(--ink);
  }
  .parents-title { font-weight: 700; font-size: 18px; line-height: 1.2; margin-bottom: 12px; }
  .parents-text { font-size: 15px; line-height: 1.35; }

  .photo-circle-bottom {
    left: 690px; top: 960px; width: 170px; height: 200px; border-radius: 50%;
    border: 5px solid var(--lime);
    background: radial-gradient(circle at 50% 45%, #f1b35c 0%, #8a5a3a 60%, #2e3a58 100%);
  }
</style>
</head>
<body>
<main class="flyer">
  <header class="brand">
    <span class="brand-dot"></span>
    <span class="brand-name">MOPVELTA</span>
  </header>

  <h1 class="title-band">High Energy Hip Hop Dance Club At Your School</h1>

  <section class="intro-panel"></section>
  <div class="slogans">
    <span>Dance is Fun!</span><span>Dance is cool!</span><span>Dance is Great Exercise!</span>
  </div>

  <div class="photo photo-circle-top" role="img" aria-label="Photo of a smiling boy dancing"></div>

  <div class="features">
    <p>Excellent for Boys and Girls.<br>No previous experience required.</p>
    <p>Warm-up, Stretch, And Move to Great Music<br>Learn group routines<br>Create your choreography</p>
  </div>

  <aside class="register-box">
    <div class="register-title">REGISTER TODAY!</div>
    <p>Online Registration:<br>Go to www.mopvelta.com</p>
    <p>Registration Hotline:<br>Call 416-729-3546 ext 517</p>
    <p>See reverse side for details</p>
  </aside>

  <div class="offer-stripe">Get a FREE dance-along DVD each term, $25 value each</div>

  <div class="photo photo-main" role="img" aria-label="Photo of a group of happy children dancing together"></div>

  <aside class="parents-column">
    <h2 class="parents-title">Important Notice to Parents</h2>
    <p class="parents-text">Educational studies confirm that children who participate in extracurricular programs enjoy an increase sense of accomplishment, competence and self-esteem, translating into improved academic performance.</p>
  </aside>

  <div class="photo photo-circle-bottom" role="img" aria-label="Photo of a child dancing"></div>
</main>
</body>
</html>
```